Graphic design for Student Conference

We need design work done for our annual student conference called Lantern Fest. We have a central logo but need design work done to use on posters, banners, etc. that tie into the theme for this year's conference. The theme is "Be Glad" and I would like the design elements to have a very fun, 1980's or 1990's vibe to them. The feeling of happiness and joy should be felt in the design.

Target Market(s)

Students 10-12 years of age

Industry/Entity Type

Church

Requirements
Must have
• Must include the Lantern Fest logo - event date: June 19-21 - event website: brightoakparish.org/lanternfest - Flexible supporting artwork elements that can be used in a variety of mediums. - Must use fonts that are available from free, open sources or can be provided upon delivery of completed project.
Should not have
• Anything crude, scary or content inappropriate for middle school students. Should not have any imagery related to a classroom or meeting.

```html
<!DOCTYPE html>
<html lang="en">
<head>
<meta charset="utf-8">
<title>Lantern Fest presents Be Glad</title>
<link rel="stylesheet" href="https://fonts.googleapis.com/css2?family=Montserrat:wght@900&family=Oswald:wght@600&family=Poppins:wght@400;600&display=swap">
<style>
  :root {
    --backdrop: #f1f0ed;
    --slate: #5f6e6c;
    --slate-deep: #4f5d5b;
    --cream: #f4dfb6;
    --tangerine: #e8703c;
    --lemon: #ebd843;
    --amber: #f6a12d;
    --gold: #f0b94a;
    --mustard: #e8c23a;
    --sunny: #f3da3b;
    --ink: #2f3433;
    --mist: #e6ddcc;
  }
  html, body {
    margin: 0;
    padding: 0;
    width: 1200px;
    height: 3021px;
    overflow: hidden;
    background: var(--backdrop);
  }
  .poster {
    position: absolute;
    left: 100px;
    top: 803px;
    width: 1000px;
    height: 1414px;
    display: block;
  }
  .event-name { font-family: "Montserrat", sans-serif; font-weight: 900; fill: var(--sunny); }
  .presents { font-family: "Poppins", sans-serif; font-weight: 400; fill: var(--sunny); letter-spacing: 14px; }
  .headline { font-family: "Montserrat", sans-serif; font-weight: 900; }
  .headline-be { fill: var(--cream); }
  .glyph-g { fill: var(--tangerine); }
  .glyph-l { fill: var(--lemon); }
  .glyph-a { fill: var(--amber); }
  .glyph-d { fill: var(--cream); }
  .date-label { font-family: "Oswald", sans-serif; font-weight: 600; fill: var(--mustard); }
  .date-range { font-family: "Poppins", sans-serif; font-weight: 600; fill: var(--gold); }
  .date-range .date-number { fill: var(--cream); }
  .host-name { font-family: "Poppins", sans-serif; font-weight: 600; fill: var(--mist); }
  .host-dot { fill: var(--mist); }
  .web-address { font-family: "Poppins", sans-serif; font-weight: 400; fill: var(--mist); letter-spacing: 2px; }
</style>
</head>
<body>
<svg class="poster" viewBox="0 0 1000 1414" xmlns="http://www.w3.org/2000/svg" aria-label="Lantern Fest presents Be Glad poster">
  <defs>
    <radialGradient id="slate-wash" cx="50%" cy="45%" r="75%">
      <stop offset="0" stop-color="var(--slate)"/>
      <stop offset="1" stop-color="var(--slate-deep)"/>
    </radialGradient>
    <linearGradient id="art-wash" x1="0" y1="0" x2="1" y2="1">
      <stop offset="0" stop-color="#3a3f3e"/>
      <stop offset="1" stop-color="#545b5a"/>
    </linearGradient>
  </defs>

  <rect class="poster-ground" width="1000" height="1414" fill="url(#slate-wash)"/>

  <text class="event-name" x="500" y="210" text-anchor="middle" font-size="74" textLength="560" lengthAdjust="spacingAndGlyphs">LANTERN FEST</text>
  <text class="presents" x="500" y="320" text-anchor="middle" font-size="28">PRESENTS</text>

  <rect class="guitar-birds-art" role="img" aria-label="Illustration of an acoustic guitar whose strings turn into a flock of dark birds flying upward" x="128" y="384" width="705" height="560" rx="24" fill="url(#art-wash)" opacity="0.55"/>

  <text class="headline headline-be" x="118" y="629" font-size="262" textLength="358" lengthAdjust="spacingAndGlyphs">BE</text>

  <g class="headline headline-glad" font-size="350">
    <text class="glyph-g" x="96" y="963" textLength="255" lengthAdjust="spacingAndGlyphs">g</text>
    <text class="glyph-l" x="353" y="963" textLength="110" lengthAdjust="spacingAndGlyphs">l</text>
    <text class="glyph-a" x="466" y="963" textLength="222" lengthAdjust="spacingAndGlyphs">a</text>
    <text class="glyph-d" x="690" y="963" textLength="240" lengthAdjust="spacingAndGlyphs">d</text>
  </g>

  <text class="date-label" x="500" y="1112" text-anchor="middle" font-size="34">EVENT DATE</text>
  <text class="date-range" x="500" y="1192" text-anchor="middle" font-size="70">JUNE <tspan class="date-number">19</tspan><tspan font-size="38" dy="-26">TH</tspan><tspan dy="26"> TO </tspan><tspan class="date-number">21</tspan><tspan font-size="38" dy="-26">TH</tspan></text>

  <circle class="host-dot" cx="378" cy="1264" r="34"/>
  <text class="host-name" x="426" y="1275" font-size="30">BRIGHT OAK PARISH</text>

  <text class="web-address" x="500" y="1348" text-anchor="middle" font-size="34">brightoakparish.org/lanternfest</text>
</svg>
</body>
</html>
```